K7Q480 brochure

We want a new brochure for our rebranding of our sports health and wellness centre. We are based in Townsville in North Queensland. We provide chiropractic, physiotherapy, massage, nutrition and yoga services. We would like to see designs and content that portray our unique one stop destination for many allied health services and our one on one functional rehab approach customised to each individual. We would like to keep colours that compliment our logo colours. The design should be professional and one that could be handed out to Medical Doctors, other referring healthcare professionals and prospective sports and active lifestyle patients. The brochure should also note that we also accept/treat Jobshield, RSB, Vitafund KPS, and Accident and Injury referrals
Updates

Please check out our website for more information on who we are and what we do. I will upload our new logo in a few moments. Cheers! Www.peakvitaro.com.au

Reason: We understand creating a quality brochure takes time and we wanted to give the creatives more time to create. With the extended deadline we are now guaranteeing the payment.

Target Market(s)

Referring Medical Doctors and other health professionals
Athletes and Active lifestyle patients
Wellness patients

Industry/Entity Type

Healthcare

Requirements
Nice to have
• Brochure can be single double sided, or bi-fold of approx. size of 210mm x 99mm
Should not have
• Brochure should not focus on or place emphasis on one particular service that we offer rather focus on the services provided as a whole.

```html
<!DOCTYPE html>
<html lang="en">
<head>
<meta charset="utf-8">
<title>K7Q480 Brochure</title>
<link href="https://fonts.googleapis.com/css2?family=Arimo:wght@400;700&display=swap" rel="stylesheet">
<style>
  :root {
    --canvas: #ffffff;
    --page-blue: #1f7fd0;
    --page-blue-light: #3b9ae4;
    --page-blue-deep: #0f63b4;
    --band-blue: #0c5fae;
    --header-glow: #5aaeea;
    --text: #ffffff;
    --brand-ink: #ffffff;
    --brand-dot: #e0224f;
    --burst-red: #e8194a;
    --photo-warm: #d9b98a;
    --photo-cool: #cfe3f2;
    --frame: #6fb6ee;
  }
  * { box-sizing: border-box; margin: 0; padding: 0; }
  html, body { width: 1200px; height: 776px; overflow: hidden; background: var(--canvas); }
  body { position: relative; font-family: "Arimo", Arial, sans-serif; color: var(--text); }

  .page {
    position: absolute;
    top: 17px;
    width: 565px;
    height: 741px;
    overflow: hidden;
    background: radial-gradient(ellipse at 60% 45%, var(--page-blue-light) 0%, var(--page-blue) 55%, var(--page-blue-deep) 100%);
  }
  .page--front { left: 17px; }
  .page--back { left: 617px; }

  .page__header {
    position: absolute; left: 0; top: 0; width: 100%; height: 125px;
    background: linear-gradient(180deg, var(--header-glow) 0%, var(--page-blue-light) 100%);
  }

  .welcome {
    position: absolute; left: 36px; top: 25px;
    font-size: 31px; font-weight: 700; letter-spacing: 0.3px;
  }

  .brand {
    position: absolute; display: flex; align-items: center; gap: 8px;
    font-size: 30px; font-weight: 700; color: var(--brand-ink); letter-spacing: 0.5px;
  }
  .brand__dot { width: 22px; height: 22px; border-radius: 50%; background: var(--brand-dot); }
  .brand--front { left: 38px; top: 78px; }
  .brand--back { left: 360px; top: 26px; }

  .heading {
    position: absolute; font-size: 22px; font-weight: 400; line-height: 1.2;
  }

  .copy {
    position: absolute;
    font-size: 9.6px; line-height: 21px; text-align: justify;
  }

  .band {
    position: absolute; top: 402px; height: 101px; background: var(--band-blue);
  }
  .band--front { left: 288px; width: 277px; }
  .band--back { left: 0; width: 565px; }

  .photo {
    position: absolute; left: 49px; top: 406px; width: 200px; height: 302px;
    border: 4px solid var(--frame);
    background: linear-gradient(180deg, var(--photo-cool) 0%, #eef3f6 45%, var(--photo-warm) 75%, #c89a63 100%);
  }

  .burst { position: absolute; left: 271px; top: 386px; width: 216px; height: 140px; }
  .burst__label {
    position: absolute; left: 271px; top: 444px; width: 216px; text-align: center;
    font-size: 19px;
  }

  .accepts {
    position: absolute; left: 302px; top: 526px; width: 238px;
    list-style: none; font-size: 14px; font-weight: 700; line-height: 41px;
  }
</style>
</head>
<body>

<section class="page page--front">
  <div class="page__header"></div>
  <h1 class="welcome">WELCOME TO</h1>
  <div class="brand brand--front"><span class="brand__dot"></span>K7Q480</div>
  <h2 class="heading" style="left:307px; top:70px;">Chiropractic Care</h2>

  <p class="copy" style="left:31px; top:145px; width:240px;">Lorem Ipsum is simply dummy text of the printing and typesetting industry. Lorem Ipsum has been the industry's standard dummy text ever since the 1500s, when an unknown printer took a galley of type and scrambled it to make a type specimen book. It has survived not only five centuries, but also the leap into electronic typesetting, remaining essentially unchanged. It was popularised in the 1960s with the release of Norvale sheets containing Lorem Ipsum passages, and more recently with desktop publishing software like Quillset Layout including versions of Lorem Ipsum.</p>

  <p class="copy" style="left:307px; top:145px; width:230px;">Lorem Ipsum is simply dummy text of the printing and typesetting industry. Lorem Ipsum has been the industry's standard dummy text ever since the 1500s, when an unknown printer took a galley of type and scrambled it to make a type specimen book. It has survived not only five centuries, but also the leap into electronic typesetting, remaining essentially unchanged. It was popularised in the 1960s with the release of Norvale sheets containing Lorem Ipsum passages, and more recently with desktop publishing software like Quillset Layout including versions of Lorem Ipsum.</p>

  <div class="photo" role="img" aria-label="Photo of a group exercise class doing push-ups on blue mats in a bright studio"></div>

  <div class="band band--front"></div>
  <h2 class="heading" style="left:317px; top:440px;">Corrective Exercises</h2>

  <p class="copy" style="left:305px; top:524px; width:230px;">Lorem Ipsum is simply dummy text of the printing and typesetting industry. Lorem Ipsum has been the industry's standard dummy text ever since the 1500s, when an unknown printer took a galley of type and scrambled it to make a type specimen book. It has survived not only five centuries, but also the leap into electronic typesetting, remaining essentially unchanged.</p>
</section>

<section class="page page--back">
  <div class="brand brand--back"><span class="brand__dot"></span>K7Q480</div>
  <h2 class="heading" style="left:34px; top:48px;">Lifestyle Advice<br>&amp; In house Yoga</h2>
  <h2 class="heading" style="left:304px; top:76px;">Massage Therapy</h2>

  <p class="copy" style="left:31px; top:145px; width:240px;">Lorem Ipsum is simply dummy text of the printing and typesetting industry. Lorem Ipsum has been the industry's standard dummy text ever since the 1500s, when an unknown printer took a galley of type and scrambled it to make a type specimen book. It has survived not only five centuries, but also the leap into electronic typesetting, remaining essentially unchanged. It was popularised in the 1960s with the release of Norvale sheets containing Lorem Ipsum passages, and more recently with desktop publishing software like Quillset Layout including versions of Lorem Ipsum.</p>

  <p class="copy" style="left:302px; top:145px; width:235px;">Lorem Ipsum is simply dummy text of the printing and typesetting industry. Lorem Ipsum has been the industry's standard dummy text ever since the 1500s, when an unknown printer took a galley of type and scrambled it to make a type specimen book. It has survived not only five centuries, but also the leap into electronic typesetting, remaining essentially unchanged.</p>

  <div class="band band--back"></div>
  <h2 class="heading" style="left:34px; top:440px;">Nutritional Counselling</h2>

  <svg class="burst" viewBox="-4 -4 224 148" aria-hidden="true">
    <polygon fill="var(--burst-red)" stroke="#ffffff" stroke-width="2"
      points="216,70 189,77.8 210.7,91.6 181.1,92.7 195.4,111.2 166,105.4 171.5,126.6 145.2,114.6 141.4,136.6 120.8,119.4 108,140 95.2,119.4 74.6,136.6 70.8,114.6 44.5,126.6 50,105.4 20.6,111.2 34.9,92.7 5.3,91.6 27,77.8 0,70 27,62.2 5.3,48.4 34.9,47.3 20.6,28.8 50,34.6 44.5,13.4 70.8,25.4 74.6,3.4 95.2,20.6 108,0 120.8,20.6 141.4,3.4 145.2,25.4 171.5,13.4 166,34.6 195.4,28.8 181.1,47.3 210.7,48.4 189,62.2"/>
  </svg>
  <div class="burst__label">More Information</div>

  <p class="copy" style="left:31px; top:524px; width:240px;">Lorem Ipsum is simply dummy text of the printing and typesetting industry. Lorem Ipsum has been the industry's standard dummy text ever since the 1500s, when an unknown printer took a galley of type and scrambled it to make a type specimen book. It has survived not only five centuries, but also the leap into electronic typesetting, remaining essentially unchanged.</p>

  <ul class="accepts">
    <li>- Accept/treat Jobshield</li>
    <li>- Accept/treat RSB</li>
    <li>- Accept/treat Vitafund KPS</li>
    <li>- Accept/treat accident and Injury referrals</li>
  </ul>
</section>

</body>
</html>
```